IT services company requires Letterhead design

We need a professional letterhead designed to be used for general correspondence with customers, quotes, invoices etc. We are a new IT services company specialising in computer servicing and repairs and mobile and tablet repairs. Attached are templates that my printing company have supplied, my logos, an interpretation of our website for you to get a feel of the company. Details to be included on the letterhead are

Company Number – 4830517
VAT Number - 581736294
Registered Address – 14-16 Brambury Lane, London, E9 3PL

Phone – 01843 572236
Email – sales@quorvant.com
Web – www.quorvant.com

I would prefer for the top of the letterhead to just have the company logo on a white background and the rest of the details on the bottom of the letterhead but I am open to design ideas.

Thanks

```html
<!DOCTYPE html>
<html lang="en">
<head>
<meta charset="utf-8">
<title>Quorvant Letterhead</title>
<link href="https://fonts.googleapis.com/css2?family=PT+Sans:wght@400;700&display=swap" rel="stylesheet">
<style>
  :root {
    --backdrop: #e6e7e9;
    --paper: #ffffff;
    --brand-blue: #31c1e4;
    --brand-dark: #3b3b3b;
    --ink: #3a3a3a;
    --ink-light: #ffffff;
  }
  * { margin: 0; padding: 0; box-sizing: border-box; }
  html, body {
    width: 1200px; height: 1200px; overflow: hidden;
    background: var(--backdrop);
    font-family: "PT Sans", "Myriad Pro", Arial, sans-serif;
  }
  .letterhead {
    position: absolute; left: 204px; top: 40px;
    width: 792px; height: 1120px;
    background: var(--paper);
    border: 1px solid #c9cacc;
  }
  .brand {
    position: absolute; left: 52px; top: 48px;
    display: flex; align-items: center; gap: 10px;
  }
  .brand-square {
    width: 18px; height: 18px; background: var(--brand-blue);
  }
  .brand-name {
    font-weight: 700; font-size: 34px; color: var(--brand-dark);
    letter-spacing: 0.5px; line-height: 1;
  }
  .footer {
    position: absolute; left: 0; bottom: 0;
    width: 100%; height: 68px;
  }
  .footer-band { position: absolute; inset: 0; width: 100%; height: 100%; }
  .company-details {
    position: absolute; left: 27px; top: 8px;
    font-size: 13px; line-height: 16.5px; color: var(--ink);
  }
  .company-details .row { display: flex; }
  .company-details .label { width: 91px; }
  .contact-details {
    position: absolute; left: 642px; top: 8px;
    font-size: 13px; line-height: 16.5px; color: var(--ink-light);
    list-style: none;
  }
  .contact-details li { display: flex; align-items: center; gap: 9px; }
  .contact-details svg { width: 11px; height: 11px; fill: var(--ink-light); flex: none; }
</style>
</head>
<body>
  <main class="letterhead">
    <header class="brand">
      <span class="brand-square"></span>
      <span class="brand-name">Quorvant</span>
    </header>

    <footer class="footer">
      <svg class="footer-band" viewBox="0 0 792 68" preserveAspectRatio="none" role="img" aria-label="Two-tone footer band, blue with a dark panel on the right">
        <rect x="0" y="0" width="792" height="68" fill="var(--brand-blue)"/>
        <polygon fill="var(--brand-dark)" points="462,0 792,0 792,68 356,68"/>
      </svg>

      <div class="company-details">
        <div class="row"><span class="label">Company No.</span><span>4830517</span></div>
        <div class="row"><span class="label">VAT No.</span><span>581736294</span></div>
        <div class="row"><span class="label">Reg. Address</span><span>14-16 Brambury Lane, London, E9 3PL</span></div>
      </div>

      <ul class="contact-details">
        <li>
          <svg viewBox="0 0 24 24"><path d="M6.6 10.8a15.1 15.1 0 0 0 6.6 6.6l2.2-2.2a1 1 0 0 1 1-.25 11.4 11.4 0 0 0 3.6.57 1 1 0 0 1 1 1V20a1 1 0 0 1-1 1A17 17 0 0 1 3 4a1 1 0 0 1 1-1h3.5a1 1 0 0 1 1 1c0 1.25.2 2.45.57 3.57a1 1 0 0 1-.25 1z"/></svg>
          <span>01843 572236</span>
        </li>
        <li>
          <svg viewBox="0 0 24 24"><path d="M2 5h20v2l-10 6L2 7z"/><path d="M2 9l10 6 10-6v10H2z"/></svg>
          <span>sales@quorvant.com</span>
        </li>
        <li>
          <svg viewBox="0 0 24 24"><circle cx="12" cy="12" r="10"/><path d="M2 12h20M12 2c3 3 3 17 0 20M12 2c-3 3-3 17 0 20" stroke="var(--brand-dark)" stroke-width="1.6" fill="none"/></svg>
          <span>www.quorvant.com</span>
        </li>
      </ul>
    </footer>
  </main>
</body>
</html>
```